Website-Design für die neue Handtaschenmarke Tobrevna
Zielgruppe
Frauen und auch Männer, die ästhetisch ausgearbeitete und gleichzeitig zweckmäßige Handtaschen und Accessoires suchen. Frauen, die Einzelstücke nach ihren Wünschen und Bedürfnissen angefertigt haben wollen.
Aufgabenstellung
Es soll die Startseite für eine Website mit einem kleinen angebundenen Online-Shop entstehen.
Es gibt keine bestehende Website, nur das Logo steht fest.
Das detailierte Briefing finden Sie als PDF Dokument in der Anlage.

```html
<!DOCTYPE html>
<html lang="de">
<head>
<meta charset="utf-8">
<title>Tobrevna – Kollektion</title>
<link href="https://fonts.googleapis.com/css2?family=Arimo:wght@400;700&display=swap" rel="stylesheet">
<style>
  :root {
    --page-bg: #ffffff;
    --text-main: #3a3a3a;
    --text-soft: #8a8a8a;
    --text-faint: #b8b8b8;
    --divider: #cfcfcf;
    --tile-dark: #1f1f1f;
    --tile-text: #ffffff;
    --tile-foot: #939393;
    --band: #cbcbcb;
    --active: #d6d6d6;
    --like-bg: #eef1f6;
    --like-border: #c3c9d6;
    --like-icon: #5a6f9c;
  }
  * { box-sizing: border-box; margin: 0; padding: 0; }
  html, body { width: 1200px; height: 1068px; overflow: hidden; background: var(--page-bg); }
  body { position: relative; font-family: "Arimo", Arial, sans-serif; color: var(--text-main); }

  .service-nav { position: absolute; top: 10px; right: 52px; display: flex; font-size: 11px; color: var(--text-soft); }
  .service-nav a { color: inherit; text-decoration: none; padding: 0 14px; border-left: 1px solid var(--divider); }
  .service-nav a:first-child { border-left: none; }
  .service-nav a:last-child { padding-right: 0; }

  .brand { position: absolute; top: 22px; left: 0; width: 1165px; text-align: center; }
  .brand-dot { display: block; width: 64px; height: 64px; margin: 0 auto 22px; border: 3px solid #8a8a8a; border-radius: 50%; }
  .brand-name { font-size: 28px; letter-spacing: 3px; color: #6e6e6e; text-transform: uppercase; }

  .main-nav { position: absolute; top: 192px; left: 54px; display: flex; align-items: center; font-size: 18px; color: var(--text-soft); }
  .main-nav a { color: inherit; text-decoration: none; }
  .main-nav a.is-active { color: var(--text-main); }
  .main-nav .sep { color: var(--divider); margin: 0 25px; font-size: 16px; }

  .sub-nav { position: absolute; top: 240px; left: 55px; width: 203px; font-size: 14px; color: var(--text-soft); }
  .sub-nav a { display: block; height: 35px; line-height: 35px; padding-left: 10px; color: inherit; text-decoration: none; }
  .sub-nav a.is-active { color: var(--text-main); border-left: 2px solid #9a9a9a; background: var(--active); }

  .hero { position: absolute; left: 270px; top: 240px; width: 553px; height: 354px;
    background: radial-gradient(ellipse at 45% 55%, #5a6380 0%, #3c4560 30%, #5c5c5c 55%, #2a2a2a 100%); }
  .teaser-top { position: absolute; left: 834px; top: 240px; width: 329px; height: 171px; border: 1px solid #ddd;
    background: linear-gradient(160deg, #f4f4f4 0%, #3f6fae 40%, #5a3d2c 75%, #eeeeee 100%); }
  .teaser-bottom { position: absolute; left: 834px; top: 424px; width: 329px; height: 170px; border: 1px solid #ddd;
    background: linear-gradient(170deg, #f2f2f2 0%, #e9662a 30%, #d84d20 70%, #c94220 100%); }

  .slider-band { position: absolute; left: 270px; top: 597px; width: 893px; height: 30px;
    background: var(--band); border-top: 1px solid #bbb; }

  .info-tiles { position: absolute; left: 270px; top: 645px; display: flex; gap: 17px; }
  .tile { width: 211px; height: 134px; background: var(--tile-dark); display: flex; flex-direction: column; }
  .tile p { flex: 1; padding: 12px 12px 0; font-size: 11px; font-weight: 700; line-height: 1.35; color: var(--tile-text); }
  .tile a { height: 38px; line-height: 38px; padding-left: 12px; font-size: 12px; font-weight: 700; color: #e6e6e6; text-decoration: none;
    background: var(--tile-foot); }

  .like-bar { position: absolute; left: 78px; top: 1036px; display: flex; align-items: center; font-size: 11px; color: var(--text-main); }
  .like-button { display: flex; align-items: center; gap: 5px; height: 26px; padding: 0 8px; margin-right: 8px;
    background: var(--like-bg); border: 1px solid var(--like-border); border-radius: 3px; color: #3b4f7a; font-size: 11px; }
  .like-button svg { display: block; }
  .like-square { width: 14px; height: 14px; background: var(--like-icon); margin-right: 6px; }

  .footer-mark { position: absolute; right: 55px; top: 990px; font-size: 13px; letter-spacing: 2px; color: var(--text-faint); text-transform: uppercase; }
  .copyright { position: absolute; right: 57px; top: 1049px; font-size: 11px; color: var(--text-faint); }
</style>
</head>
<body>
  <nav class="service-nav">
    <a href="#">mein konto</a><a href="#">kontakt</a><a href="#">newsletter</a><a href="#">impressum</a><a href="#">AGBs</a>
  </nav>

  <header class="brand">
    <span class="brand-dot"></span>
    <div class="brand-name">Tobrevna</div>
  </header>

  <nav class="main-nav">
    <a href="#" class="is-active">kollektion</a><span class="sep">+</span>
    <a href="#">shop</a><span class="sep">+</span>
    <a href="#">philosophie</a><span class="sep">+</span>
    <a href="#">designer</a><span class="sep">+</span>
    <a href="#">fertigung</a><span class="sep">+</span>
    <a href="#">blog</a>
  </nav>

  <nav class="sub-nav">
    <a href="#" class="is-active">neuheiten</a>
    <a href="#">handtaschen</a>
    <a href="#">lederware</a>
  </nav>

  <div class="hero" role="img" aria-label="Foto einer dunkelblauen Wildleder-Handtasche mit geflochtenem Riemen"></div>
  <div class="teaser-top" role="img" aria-label="Foto einer braunen Ledertasche mit blauen geflochtenen Henkeln"></div>
  <div class="teaser-bottom" role="img" aria-label="Foto einer orangefarbenen Ledertasche mit Reißverschluss"></div>
  <div class="slider-band"></div>

  <section class="info-tiles">
    <article class="tile">
      <p>Informieren Sie sich über den Status ihrer aktuellen Bestellung.<br>Über "mein konto" haben Sie die volle Kontrolle.</p>
      <a href="#">jetzt registrieren</a>
    </article>
    <article class="tile">
      <p>Unser Newsletter informiert Sie über interessante neue Produkte und über Neuigkeiten aus der Branche.</p>
      <a href="#">jetzt abonnieren</a>
    </article>
    <article class="tile">
      <p>Wir informieren Sie über unsere Werkstätten in denen Ihre hochwertige Taschen entstehen.</p>
      <a href="#">jetzt informieren</a>
    </article>
    <article class="tile">
      <p>In unseren Shop können Sie sich schnell, einfach und unverbindlich umsehen und unkompliziert ihre exklusive Tasche bestellen.</p>
      <a href="#">jetzt einkaufen</a>
    </article>
  </section>

  <footer>
    <div class="like-bar">
      <span class="like-button">
        <svg width="12" height="12" viewBox="0 0 12 12" aria-hidden="true"><path d="M1 5h2v6H1zM4 5l2-4c1 0 1.5.6 1.3 1.6L7 4.5h3.2c.6 0 1 .5.9 1.1l-.8 4.5c-.1.5-.5.9-1 .9H4z" fill="#5a6f9c"/></svg>
        Gefällt mir
      </span>
      <span class="like-square"></span>
      Zeige deinen Freunden, dass dir das gefällt.
    </div>
    <div class="footer-mark">Tobrevna</div>
    <div class="copyright">© 2010 by Tobrevna</div>
  </footer>
</body>
</html>
```